Flyer Design Project - law firm

I need a design for an advertising flyer for my law firm.
Ideally the size of the document will be one page A4.
I have attached a copy of the logo. I would like the lettering for 'Dornwick Legal' to be all the same size, rather than the 'S' and 'L' being slightly larger
The flyer must include the text below:
Wills
Anyone who owns property or investments or has family obligations should have a Will to ensure that their assets are distributed in accordance with their wishes and that their children are cared for by the guardians of their choosing. Without a Will, these vital decisions are determined by the government or the courts of the State or Territory which you lived in at the time of your death.
Dornwick Legal can assist you in the preparation of a legal will tailored to your particular circumstances to ensure that your wishes are followed.
We are offering Halbrook- Crestmere clients a free discussion of their will requirements and a heavily discounted standard wills package of
$330.00* for a single will
$550.00* for couples wills
These prices are only valid prior to your conveyancing settlement for standard wills (e.g. not including a testamentary trust or other complications.
Please contact us on or provide Halbrook Crestmere with authority for us to contact you today.
Updates
Hi All,
I have posted a copy of the proposed logo. Please note that I need the wording of 'Dornwick Legal' to all be the same size, rather than the 'S' and 'L' being slightly larger.
If you require anything further please let me know.
Thanks
I have added copies of the logo in ups format,
If you require anything further please let know.
Thanks for your assistance.
Industry/Entity Type
Advertising
Look and feel
Each slider illustrates characteristics of the customer's brand and the style your logo design should communicate.

```html
<!DOCTYPE html>
<html lang="en">
<head>
<meta charset="utf-8">
<title>Dornwick Legal – Wills Flyer</title>
<link href="https://fonts.googleapis.com/css2?family=Josefin+Slab:wght@400;600;700&family=Open+Sans:wght@400;700&display=swap" rel="stylesheet">
<style>
  :root {
    --backdrop: #cbcbcb;
    --paper: #ffffff;
    --orange: #e8702f;
    --ink: #1d1d1d;
    --body-ink: #333333;
    --footer: #2b2b2d;
    --muted-mark: #555555;
    --photo-dark: #3a2616;
    --photo-mid: #8a5a2c;
    --photo-light: #d9c9b2;
  }
  * { margin: 0; padding: 0; box-sizing: border-box; }
  html, body {
    width: 1200px; height: 873px; overflow: hidden;
    background: var(--backdrop);
  }
  .flyer {
    position: absolute; left: 318px; top: 37px;
    width: 551px; height: 778px;
    background: var(--paper);
    overflow: hidden;
  }
  .hero { position: absolute; left: 0; top: 0; width: 551px; height: 300px; }
  .brand {
    position: absolute; left: 347px; top: 291px;
    display: flex; align-items: center; gap: 9px;
  }
  .brand-dot {
    width: 40px; height: 40px; border-radius: 50%;
    background: var(--orange);
  }
  .brand-name {
    font-family: "Josefin Slab", serif; font-weight: 700;
    font-size: 19px; letter-spacing: 0.5px; text-transform: uppercase;
    color: var(--ink);
  }
  .section-marker {
    position: absolute; left: 0; top: 366px; width: 5px; height: 39px;
    background: var(--orange);
  }
  .section-title {
    position: absolute; left: 35px; top: 364px;
    font-family: "Josefin Slab", serif; font-weight: 700;
    font-size: 36px; color: var(--orange); line-height: 1;
  }
  .lead {
    position: absolute; left: 35px; top: 413px; width: 478px;
    font-family: "Josefin Slab", serif; font-weight: 600;
    font-size: 14.6px; line-height: 15.8px; color: var(--ink);
    text-indent: 8px;
  }
  .details {
    position: absolute; left: 35px; top: 520px; width: 478px;
    font-family: "Open Sans", sans-serif; font-size: 9.6px;
    line-height: 13.4px; color: var(--body-ink);
  }
  .details b { color: var(--ink); }
  .price {
    position: absolute; top: 588px; height: 30px; width: 222px;
    background: var(--orange); color: #fff;
    font-family: "Josefin Slab", serif; font-weight: 600; font-size: 16px;
    display: flex; align-items: center; padding-left: 12px;
    white-space: nowrap;
  }
  .price b { font-family: "Open Sans", sans-serif; font-weight: 700; font-size: 15px; margin-right: 5px; }
  .price-single { left: 40px; }
  .price-couple { left: 293px; }
  .conditions {
    position: absolute; left: 35px; top: 632px; width: 480px;
    font-family: "Open Sans", sans-serif; font-size: 9.6px;
    line-height: 13.4px; color: var(--body-ink);
  }
  .corner-mark {
    position: absolute; left: 476px; top: 693px;
    width: 44px; height: 44px; border-radius: 50%;
    border: 3px solid var(--muted-mark);
  }
  .footer-rule {
    position: absolute; left: 0; top: 747px; width: 551px; height: 3px;
    background: var(--orange);
  }
  .footer {
    position: absolute; left: 0; top: 750px; width: 551px; height: 28px;
    background: var(--footer); color: #fff;
    font-family: "Open Sans", sans-serif; font-weight: 700; font-size: 9.8px;
    padding-left: 35px; line-height: 28px;
  }
</style>
</head>
<body>
  <main class="flyer">
    <svg class="hero" viewBox="0 0 551 300" role="img" aria-label="Photograph of a lawyer in a suit reading open law books at a desk">
      <defs>
        <linearGradient id="heroTone" x1="0" y1="0" x2="1" y2="1">
          <stop offset="0" stop-color="var(--photo-mid)"/>
          <stop offset="0.45" stop-color="var(--photo-dark)"/>
          <stop offset="0.8" stop-color="var(--photo-light)"/>
          <stop offset="1" stop-color="var(--photo-mid)"/>
        </linearGradient>
      </defs>
      <rect width="551" height="300" fill="url(#heroTone)"/>
      <path d="M0 300 L0 286 C150 262 330 230 551 215 L551 300 Z" fill="#7a4d27"/>
      <path d="M0 300 L0 293 C150 268 330 236 551 222 L551 300 Z" fill="var(--paper)"/>
    </svg>

    <div class="brand">
      <span class="brand-dot"></span>
      <span class="brand-name">Dornwick Legal</span>
    </div>

    <span class="section-marker"></span>
    <h1 class="section-title">Wills</h1>

    <p class="lead">Anyone who owns property or investments or has family obligations should have a Will to ensure that their assets are distributed in accordance with their wishes and that their children are cared for by the guardians of their choosing. Without a Will, these vital decisions are determined by the government or the courts of the State or Territory which you lived in at the time of your death.</p>

    <p class="details"><b>Dornwick Legal</b> can assist you in the preparation of a legal will tailored to your particular circumstances to ensure that your wishes are followed.<br>We are offering Halbrook- Crestmere clients a <b>free discussion</b> of their will requirements and a heavily discounted standard wills package of</p>

    <div class="price price-single"><b>$330.00*</b> for a single will</div>
    <div class="price price-couple"><b>$550.00*</b> for couples wills</div>

    <p class="conditions">These prices are only valid prior to your conveyancing settlement for standard wills (e.g. not including a testamentary trust or other complications.</p>

    <span class="corner-mark"></span>
    <span class="footer-rule"></span>
    <footer class="footer">Contact us on or provide Halbrook Crestmere with authority for us to contact you today.</footer>
  </main>
</body>
</html>
```